Magician | Speaker looks for an innovative business card design

I'm a magician and public speaker offering artistic and modern magical experiences.
I'm based in Brussels (Belgium.) I love magic performed up-close, creating a space of intimacy, even when I'm on stage.
The final design should communicate professionalism, elegance, artistry, and a friendly kind personality

I would like to see designs based either on my photos and/or the way I sign my name Remy Vok (see attached files for more info.)
Additional photos and more info about what I offer can be seen at www.remy-vok.net

My current business card design is also attached. I like the fact that the reverse of my current design includes quotes from master magicians about magic, changing the way my participants see the art of magic.

Note: I would like a double-sided card design. However, I need white space on the reverse to be able to write things on for my performances.

Details to include on the card:
Artist name: Remy Vok
Offer: magician + (public) speaker or magic + (public) speaking (the + sign can be replaced by another character, like a bullet or a pipe)
Phone: +32 471 265 903
Email: book@remy-vok.net
(optional) Website: www.remy-vok.net or remy-vok.net

Target Market(s)

Corporate, organisations, companies as well as individuals

Industry/Entity Type

Artists

Colors

Designer to choose colors to be used in the design.

Requirements
Nice to have
• A side with a mirror could be nice

```html
<!DOCTYPE html>
<html lang="en">
<head>
<meta charset="utf-8">
<title>Remy Vok – Business Card</title>
<link rel="stylesheet" href="https://fonts.googleapis.com/css2?family=Source+Sans+3:wght@400;600&display=swap">
<style>
  :root {
    --silver-dark: #9c9c9c;
    --silver-mid: #c9c9c9;
    --silver-light: #ffffff;
    --ink: #111111;
    --wine: #7b2a31;
    --curtain: #6e1e2a;
    --curtain-dark: #2a0c12;
    --paper: #ffffff;
    --text: #1e1e1e;
  }
  html, body {
    margin: 0;
    padding: 0;
    width: 1076px;
    height: 1200px;
    overflow: hidden;
    background: var(--paper);
    font-family: "Source Sans 3", Arial, sans-serif;
  }
  .canvas {
    position: relative;
    width: 1076px;
    height: 1200px;
  }
  .card-front {
    position: absolute;
    left: 0; top: 0;
    width: 1076px; height: 584px;
    background: linear-gradient(160deg,
      var(--silver-dark) 0%, var(--silver-mid) 22%, var(--silver-light) 38%,
      var(--silver-dark) 55%, var(--silver-light) 72%, var(--silver-mid) 85%, var(--silver-dark) 100%);
    display: flex;
    align-items: center;
    justify-content: center;
  }
  .front-name {
    font-weight: 600;
    font-size: 96px;
    color: var(--ink);
    letter-spacing: 2px;
    margin-top: 20px;
  }
  .card-back {
    position: absolute;
    left: 0; top: 584px;
    width: 1076px; height: 616px;
  }
  .portrait {
    position: absolute;
    left: 0; top: 0;
    width: 410px; height: 616px;
    background: radial-gradient(ellipse at 45% 50%, var(--curtain) 0%, #4a1420 55%, var(--curtain-dark) 100%);
  }
  .details {
    position: absolute;
    left: 410px; top: 0;
    width: 666px; height: 616px;
    background: var(--paper);
    text-align: center;
    color: var(--text);
  }
  .back-name {
    position: absolute;
    left: 0; right: 0; top: 72px;
    font-weight: 600;
    font-size: 48px;
    color: var(--wine);
    line-height: 1;
  }
  .offer {
    position: absolute;
    left: 0; right: 0; top: 176px;
    font-size: 25px;
    letter-spacing: 0.3px;
  }
  .contact-icon {
    position: absolute;
    left: 309px;
    width: 48px; height: 48px;
  }
  .contact-text {
    position: absolute;
    left: 0; right: 0;
    font-size: 25px;
    line-height: 1;
  }
  .icon-phone { top: 244px; }
  .text-phone { top: 312px; }
  .icon-mail  { top: 370px; }
  .text-mail  { top: 422px; }
  .icon-web   { top: 474px; }
  .text-web   { top: 532px; }
</style>
</head>
<body>
<div class="canvas">
  <section class="card-front">
    <div class="front-name">Remy Vok</div>
  </section>

  <section class="card-back">
    <div class="portrait" role="img" aria-label="Photo of the magician holding up a coin in front of a dark red curtain"></div>

    <div class="details">
      <div class="back-name">Remy Vok</div>
      <div class="offer">MAGICIAN AND PUBLIC SPEAKER</div>

      <svg class="contact-icon icon-phone" viewBox="0 0 48 48" fill="none" stroke="var(--wine)" stroke-width="2.4" stroke-linejoin="round">
        <path d="M8 6 L16 4 L21 15 L16 19 C19 26 23 30 30 33 L34 28 L45 33 L43 41 C40 45 34 45 28 42 C18 37 11 30 6 20 C3 14 4 9 8 6 Z"/>
      </svg>
      <div class="contact-text text-phone">+32 471 265 903</div>

      <svg class="contact-icon icon-mail" viewBox="0 0 48 48" fill="none" stroke="var(--wine)" stroke-width="2.4">
        <rect x="3" y="9" width="42" height="30"/>
        <path d="M3 9 L24 27 L45 9 M3 39 L19 23 M45 39 L29 23"/>
      </svg>
      <div class="contact-text text-mail">book@remy-vok.net</div>

      <svg class="contact-icon icon-web" viewBox="0 0 48 48" fill="none" stroke="var(--wine)" stroke-width="2.4">
        <circle cx="24" cy="24" r="21"/>
        <ellipse cx="24" cy="24" rx="9" ry="21"/>
        <path d="M24 3 V45 M3 24 H45 M7 13 H41 M7 35 H41"/>
      </svg>
      <div class="contact-text text-web">www.remy-vok.net</div>
    </div>
  </section>
</div>
</body>
</html>
```